Music Business Adviser Needs a Book Cover Design

I need a cover design for my new book called 'The Working Stage Performer: A Field Manual for Going Professional'. I am an accountant and tax lawyer specialising in advising international music artists. This book is designed to help music artists and bands navigate through the business world. I would like to see designs that would appeal to young artists, the book needs to be bold and stand out from the crowd, for example it will attract people on Brightcart through its enticing cover.

I am open to you providing creative input on the design, although I like the colour green and think this would perhaps communicate subtly financial safety and growth. The cover should clearly communicate the book is for people in the music industry.

Target Market(s)

Males and females aged between 16 and 30; their hobbies and interest are music; they perform and record music; all genres of music

Industry/Entity Type

Lawyer

Font styles to use
Sans Serif

Requirements
Must have
• Must have the title clearly stated: 'The Working Stage Performer: A Field Manual for Going Professional'. It must also have my name as author on the front: 'Gareth L. Moody'
Nice to have
• I have uploaded an image of the type of artwork, that should be on the book. I like this style - so please keep it simple, not an over complicated design.
Should not have
• Photographs of bands or musicians

```html
<!DOCTYPE html>
<html lang="en">
<head>
<meta charset="utf-8">
<title>The Working Stage Performer – Book Cover</title>
<link href="https://fonts.googleapis.com/css2?family=Oswald:wght@600&family=Tinos:wght@400;700&display=swap" rel="stylesheet">
<style>
  :root {
    --stage-bg: #dde4ea;
    --paper: #ececea;
    --paper-shade: #d9d9d6;
    --green: #1f9a60;
    --green-dark: #137447;
    --ink: #1c1c1c;
    --ink-soft: #3a3a3a;
  }
  * { margin: 0; padding: 0; box-sizing: border-box; }
  html, body { width: 1200px; height: 900px; overflow: hidden; }
  body { background: var(--stage-bg); position: relative; font-family: "Tinos", "Times New Roman", serif; color: var(--ink); }

  .book-wrap {
    position: absolute; left: 90px; top: 90px;
    width: 1020px; height: 720px;
    display: flex;
    box-shadow: 0 10px 30px rgba(0,0,0,.18);
  }
  .back-cover, .front-cover {
    position: relative; width: 480px; height: 720px;
    background: radial-gradient(ellipse at 50% 40%, var(--paper) 0%, var(--paper-shade) 100%);
  }
  .spine {
    position: relative; width: 60px; height: 720px;
    background: var(--green);
    border-left: 3px solid var(--green-dark);
    border-right: 3px solid var(--green-dark);
    display: flex; flex-direction: column; justify-content: space-between; align-items: center;
    padding: 22px 0;
  }
  .spine-text { writing-mode: vertical-rl; color: var(--ink); font-size: 20px; white-space: nowrap; }
  .spine-subtitle { font-size: 18px; }
  .spine-title { font-size: 22px; }

  /* Back cover */
  .ornament { position: absolute; border-radius: 6px; }
  .ornament-back-top { left: 250px; top: 24px; width: 110px; height: 110px;
    background: radial-gradient(circle, #b9c9c0 0%, rgba(217,217,214,0) 70%); }
  .ornament-back-bottom { left: 150px; top: 590px; width: 110px; height: 120px;
    background: radial-gradient(circle, #b9c9c0 0%, rgba(217,217,214,0) 70%); }

  .author-photo {
    position: absolute; left: 30px; top: 215px; width: 150px; height: 170px;
    background: var(--green);
  }
  .author-photo-label { position: absolute; left: 4px; top: -14px; font-size: 10px; color: var(--ink-soft); }

  .blurb { font-size: 12px; line-height: 1.45; color: var(--ink-soft); }
  .blurb-intro { position: absolute; left: 200px; top: 165px; width: 250px; }
  .blurb-intro p + p { margin-top: 8px; }
  .blurb-main { position: absolute; left: 30px; top: 420px; width: 420px; }

  /* Front cover */
  .author-name { position: absolute; left: 120px; top: 26px; width: 120px; text-align: center; font-size: 17px; }
  .author-rule { position: absolute; left: 130px; top: 50px; width: 100px; height: 4px; background: var(--ink); }
  .author-rule::after { content: ""; position: absolute; left: 0; right: 0; top: 6px; height: 1px; background: var(--ink); }
  .ornament-front-small { left: 160px; top: 62px; width: 40px; height: 50px;
    background: linear-gradient(180deg, #5a5a5a, #6fb894); border-radius: 4px; }

  .front-title {
    position: absolute; left: 20px; top: 140px; width: 440px; text-align: center;
    font-family: "Oswald", "Arial Narrow", sans-serif; font-weight: 600;
    font-size: 40px; color: var(--green); line-height: 1.1;
  }
  .front-subtitle {
    position: absolute; left: 20px; top: 225px; width: 440px; text-align: center;
    font-size: 32px; line-height: 1.45; color: var(--ink);
  }
  .front-artwork {
    position: absolute; left: 230px; top: 430px; width: 240px; height: 270px;
    background: linear-gradient(135deg, rgba(111,184,148,.5) 0%, #6fb894 40%, #1a1a1a 80%);
    border-radius: 10px;
  }
</style>
</head>
<body>
  <main class="book-wrap">
    <section class="back-cover">
      <div class="ornament ornament-back-top" role="img" aria-label="Swirling treble clef ornament in grey and green"></div>

      <div class="author-photo">
        <span class="author-photo-label">Author Picture</span>
      </div>

      <div class="blurb blurb-intro">
        <p>The music industry is shapeshifting. Music artists must work harder than ever to make a career of their creative mastery.</p>
        <p>As an artist you are not in a typical profession but you can be big business. A good business mindset starts with making sure you understand that you are a business and that you will need the right team on board to help you navigate the legal complexities of the business world.</p>
      </div>

      <p class="blurb blurb-main">Whilst you may have a fine mix of talent in terms of your manager and record label, success won't be guaranteed unless you have a first rate line of defence to help protect your earnings. This book provides an easy to understand overview of setting up in business for the first time, some practical tips on getting started, as well as a discussion of the business challenges you'll face along your journey to becoming an international superstar.</p>

      <div class="ornament ornament-back-bottom" role="img" aria-label="Swirling treble clef ornament in grey and green"></div>
    </section>

    <section class="spine">
      <span class="spine-text spine-subtitle">A Field Manual for Going Professional</span>
      <span class="spine-text spine-title">The Working Stage Performer</span>
    </section>

    <section class="front-cover">
      <p class="author-name">Gareth L. Moody</p>
      <div class="author-rule"></div>
      <div class="ornament ornament-front-small" role="img" aria-label="Small music note ornament"></div>

      <h1 class="front-title">The Working Stage Performer</h1>
      <h2 class="front-subtitle">A Field Manual for<br>Going Professional</h2>

      <div class="front-artwork" role="img" aria-label="Illustration of music notes and a treble clef flowing from a dark silhouette"></div>
    </section>
  </main>
</body>
</html>
```